Quillon Maison Wood Fired Pizza business card design

I have a logo and need an eye catching design that will get me noticed.
My business is wood fired pizza. I want a bold design that will make our customers remember us and the food that we serve. Work with the colors of our logo and texts. Maybe add designs that lend to what or how pizza is made using our wood fired oven?

Target Market(s)

Foodies!

Contact Information for Business Card

Quillon Maison Wood Fired Pizza
Our slogan is Fast. Fresh. Handcrafted
Catering for all events

Requirements
Must have
• Dana Porrick
Telephone 570 555 0183
website www.getquillon.example
Facebook @getquillonpizza maybe use the facebook logo next to it
Instagram getquillonpizza maybe use the instagram logo next to it
Catering for all events
Nice to have
• Maybe pizza peels, pizza cutters? Wood? Fired wood? Using our flame in the background?
Please work with different colored text so each sentence stands out? A themed color for facebook?
Maybe work with the colors within our logo?
Please try to use the our quillon font, but not a must have.

```html
<!DOCTYPE html>
<html lang="en">
<head>
<meta charset="utf-8">
<title>Quillon Maison Wood Fired Pizza – Business Card</title>
<link rel="stylesheet" href="https://fonts.googleapis.com/css2?family=Oswald:wght@400;500&family=Arimo:wght@400&display=swap">
<style>
  :root {
    --page-bg: #0d0d0d;
    --card-bg: #1d1d1d;
    --flame-red: #d4151b;
    --ember-orange: #f39a1e;
    --ash-white: #e9e9e9;
    --divider: #4a4a4a;
  }
  * { box-sizing: border-box; margin: 0; padding: 0; }
  html, body {
    width: 1200px; height: 900px; overflow: hidden;
    background: var(--page-bg);
  }
  .sheet {
    width: 1200px; height: 900px;
    display: flex; flex-direction: column; align-items: center; justify-content: center;
    gap: 40px;
  }
  .card {
    width: 700px; height: 400px;
    background: var(--card-bg);
    position: relative;
    box-shadow: 0 10px 30px rgba(0,0,0,.6);
  }
  .card__divider {
    position: absolute; top: 95px; width: 1px; height: 210px;
    background: var(--divider);
  }
  /* front */
  .brand {
    position: absolute; left: 70px; top: 0; width: 270px; height: 400px;
    display: flex; align-items: center; justify-content: center; gap: 14px;
  }
  .brand__dot {
    width: 26px; height: 26px; border-radius: 50%;
    background: var(--flame-red); flex: none;
  }
  .brand__name {
    font-family: "Oswald", sans-serif; font-weight: 500;
    font-size: 38px; letter-spacing: 2px; text-transform: uppercase;
    color: var(--ash-white); line-height: 1.05;
  }
  .card--front .card__divider { left: 385px; }
  .slogan {
    position: absolute; left: 425px; top: 105px;
    font-family: "Oswald", sans-serif; font-weight: 400;
    font-size: 37px; line-height: 46px; text-transform: uppercase;
    color: var(--ember-orange);
  }
  /* back */
  .holder {
    position: absolute; left: 110px; top: 150px;
    font-family: "Oswald", sans-serif; font-weight: 400;
    font-size: 36px; text-transform: uppercase; color: var(--flame-red);
  }
  .card--back .card__divider { left: 330px; }
  .contact {
    position: absolute; left: 365px; top: 140px; list-style: none;
    font-family: "Arimo", sans-serif; font-size: 19px; color: var(--ash-white);
  }
  .contact__item { display: flex; align-items: center; gap: 12px; height: 30px; }
  .contact__icon { width: 18px; height: 18px; flex: none; }
  .contact__mark { width: 17px; height: 17px; flex: none; background: var(--flame-red); border-radius: 3px; }
  .contact__mark--round { border-radius: 50%; }
</style>
</head>
<body>
<main class="sheet">
  <section class="card card--front">
    <div class="brand">
      <span class="brand__dot"></span>
      <span class="brand__name">Quillon<br>Maison</span>
    </div>
    <span class="card__divider"></span>
    <p class="slogan">Fast. Fresh.<br>Handcrafted<br>Catering for<br>all events</p>
  </section>

  <section class="card card--back">
    <h1 class="holder">Dana Porrick</h1>
    <span class="card__divider"></span>
    <ul class="contact">
      <li class="contact__item">
        <svg class="contact__icon" viewBox="0 0 24 24" aria-hidden="true"><path fill="var(--flame-red)" d="M6.6 10.8a15.1 15.1 0 0 0 6.6 6.6l2.2-2.2a1 1 0 0 1 1-.25 11.4 11.4 0 0 0 3.6.57 1 1 0 0 1 1 1V20a1 1 0 0 1-1 1A17 17 0 0 1 3 4a1 1 0 0 1 1-1h3.5a1 1 0 0 1 1 1c0 1.25.2 2.46.57 3.6a1 1 0 0 1-.25 1z"/></svg>
        570 555 0183
      </li>
      <li class="contact__item">
        <svg class="contact__icon" viewBox="0 0 24 24" aria-hidden="true"><rect x="2" y="5" width="20" height="14" fill="var(--flame-red)"/><path d="M2 5l10 8 10-8" fill="none" stroke="var(--card-bg)" stroke-width="1.6"/></svg>
        www.getquillon.example
      </li>
      <li class="contact__item">
        <span class="contact__mark contact__mark--round"></span>
        @getquillonpizza
      </li>
      <li class="contact__item">
        <span class="contact__mark"></span>
        getquillonpizza
      </li>
    </ul>
  </section>
</main>
</body>
</html>
```